Redesign of iOS App Lumo Tutor

Redesign of existing App Lumo Tutor, an app that helps learning Japanese Kanjis, Hiragana, Katakana.

The functionallity should remain the same as today: the app is free, you may download it at the app store. But: I like the design of my other apps better ;)

Target Market(s)

Students learning Japanese

Industry/Entity Type

Teacher

Font styles to use
Sans Serif

Requirements
Must have
• Lumo Tutor has 7 main screens, all screens has to be designed for iPhone and iPad: Main, Settings, Reading Tests, Writing Tests, Game, Paper Mode, Search
Nice to have
• I like the logo as it is today

```html
<!DOCTYPE html>
<html lang="en">
<head>
<meta charset="utf-8">
<title>Lumo Tutor – Search</title>
<link rel="stylesheet" href="https://fonts.googleapis.com/css2?family=Lato:wght@400;700&family=Noto+Sans+JP:wght@300;400&display=swap">
<style>
  :root {
    --page-bg: #ececec;
    --bar-tan: #cdb28c;
    --bar-text: #3b3026;
    --list-bg: #ffffff;
    --kana: #a8895e;
    --accent: #b8996c;
    --label: #2b2b2b;
    --muted: #8a8a8a;
    --divider: #e3dccf;
  }
  * { box-sizing: border-box; margin: 0; padding: 0; }
  html, body {
    width: 730px; height: 1200px; overflow: hidden;
    background: var(--page-bg);
    font-family: "Lato", "Noto Sans JP", sans-serif;
  }
  .screen {
    width: 730px; height: 1200px;
    display: flex; flex-direction: column;
    background: var(--list-bg);
  }
  .status-bar {
    height: 40px; background: var(--bar-tan);
    display: flex; align-items: center; justify-content: space-between;
    padding: 0 16px; font-size: 17px; color: var(--bar-text);
  }
  .status-bar .carrier { display: flex; align-items: center; gap: 6px; }
  .status-bar .time { font-weight: 700; }
  .status-bar .battery { display: flex; align-items: center; gap: 6px; }
  .nav-bar {
    height: 92px; background: var(--bar-tan);
    display: flex; align-items: center; justify-content: space-between;
    padding: 0 28px; font-size: 26px; color: var(--bar-text);
    border-bottom: 1px solid #b89d77;
  }
  .nav-bar .search { display: flex; align-items: center; gap: 12px; }
  .entry-list { flex: 1; display: flex; flex-direction: column; list-style: none; }
  .entry {
    flex: 1; display: grid;
    grid-template-columns: 140px 140px 1fr 120px 100px;
    align-items: center; padding-left: 40px;
    border-bottom: 1px solid var(--divider);
  }
  .entry .kana {
    font-family: "Noto Sans JP", sans-serif; font-weight: 300;
    font-size: 68px; color: var(--kana); line-height: 1;
  }
  .entry .reading {
    display: flex; flex-direction: column; align-items: flex-start;
    color: var(--kana); font-size: 17px; gap: 4px; padding-left: 8px;
  }
  .entry .reading svg { display: block; }
  .entry .script { font-size: 20px; font-weight: 700; color: var(--label); }
  .entry .grade { font-size: 22px; color: var(--muted); }
  .entry .favourite { display: flex; justify-content: center; }
  .tab-bar {
    height: 110px; background: var(--bar-tan);
    display: flex; align-items: center; justify-content: space-between;
    padding: 0 28px 0 26px; color: var(--bar-text); font-size: 24px;
  }
  .tab-bar .home-button {
    border: 2px solid var(--bar-text); padding: 10px 16px; font-size: 22px;
  }
  .tab-bar .count { display: flex; align-items: center; gap: 14px; }
</style>
</head>
<body>
<main class="screen">
  <div class="status-bar">
    <span class="carrier">
      <svg width="54" height="10" viewBox="0 0 54 10"><g fill="#3b3026"><circle cx="5" cy="5" r="4"/><circle cx="15" cy="5" r="4"/><circle cx="25" cy="5" r="4"/><circle cx="35" cy="5" r="4"/><circle cx="45" cy="5" r="4" fill="none" stroke="#3b3026"/></g></svg>
      Nimbus
      <svg width="20" height="14" viewBox="0 0 20 14"><path d="M10 13 L2 5 A11 11 0 0 1 18 5 Z" fill="#3b3026"/></svg>
    </span>
    <span class="time">1:23 AM</span>
    <span class="battery">77%
      <svg width="44" height="18" viewBox="0 0 44 18"><rect x="1" y="1" width="38" height="16" rx="3" fill="none" stroke="#3b3026" stroke-width="1.5"/><rect x="3" y="3" width="27" height="12" rx="1.5" fill="#3b3026"/><rect x="40" y="6" width="3" height="6" rx="1" fill="#3b3026"/></svg>
    </span>
  </div>

  <header class="nav-bar">
    <span class="search">
      <svg width="28" height="28" viewBox="0 0 28 28"><circle cx="11" cy="11" r="8.5" fill="none" stroke="#3b3026" stroke-width="2.5"/><line x1="17.5" y1="17.5" x2="26" y2="26" stroke="#3b3026" stroke-width="2.5" stroke-linecap="round"/></svg>
      Search
    </span>
    <span class="help">Help</span>
  </header>

  <ul class="entry-list">
    <li class="entry"><span class="kana">あ</span><span class="reading">a<svg width="22" height="14" viewBox="0 0 22 14"><g fill="#b8996c"><circle cx="3" cy="3" r="2.2"/><circle cx="3" cy="11" r="2.2"/><circle cx="11" cy="11" r="2.2"/><circle cx="19" cy="11" r="2.2"/></g></svg></span><span class="script">Hiragana</span><span class="grade">K</span><span class="favourite"><svg width="30" height="30" viewBox="0 0 24 24"><path d="M12 2l2.9 6.6 7.1.6-5.4 4.7 1.6 7-6.2-3.7-6.2 3.7 1.6-7L2 9.2l7.1-.6z" fill="none" stroke="#b8996c" stroke-width="1.4" stroke-linejoin="round"/></svg></span></li>
    <li class="entry"><span class="kana">い</span><span class="reading">i<svg width="22" height="14" viewBox="0 0 22 14"><g fill="#b8996c"><circle cx="3" cy="3" r="2.2"/><circle cx="3" cy="11" r="2.2"/><circle cx="11" cy="11" r="2.2"/><circle cx="19" cy="11" r="2.2"/></g></svg></span><span class="script">Hiragana</span><span class="grade">K</span><span class="favourite"><svg width="30" height="30" viewBox="0 0 24 24"><path d="M12 2l2.9 6.6 7.1.6-5.4 4.7 1.6 7-6.2-3.7-6.2 3.7 1.6-7L2 9.2l7.1-.6z" fill="#b8996c" stroke="#b8996c" stroke-width="1.4" stroke-linejoin="round"/></svg></span></li>
    <li class="entry"><span class="kana">う</span><span class="reading">u<svg width="22" height="14" viewBox="0 0 22 14"><g fill="#b8996c"><circle cx="3" cy="3" r="2.2"/><circle cx="3" cy="11" r="2.2"/><circle cx="11" cy="11" r="2.2"/><circle cx="19" cy="11" r="2.2"/></g></svg></span><span class="script">Hiragana</span><span class="grade">K</span><span class="favourite"><svg width="30" height="30" viewBox="0 0 24 24"><path d="M12 2l2.9 6.6 7.1.6-5.4 4.7 1.6 7-6.2-3.7-6.2 3.7 1.6-7L2 9.2l7.1-.6z" fill="none" stroke="#b8996c" stroke-width="1.4" stroke-linejoin="round"/></svg></span></li>
    <li class="entry"><span class="kana">え</span><span class="reading">e<svg width="22" height="14" viewBox="0 0 22 14"><g fill="#b8996c"><circle cx="3" cy="3" r="2.2"/><circle cx="3" cy="11" r="2.2"/><circle cx="11" cy="11" r="2.2"/><circle cx="19" cy="11" r="2.2"/></g></svg></span><span class="script">Hiragana</span><span class="grade">K</span><span class="favourite"><svg width="30" height="30" viewBox="0 0 24 24"><path d="M12 2l2.9 6.6 7.1.6-5.4 4.7 1.6 7-6.2-3.7-6.2 3.7 1.6-7L2 9.2l7.1-.6z" fill="#b8996c" stroke="#b8996c" stroke-width="1.4" stroke-linejoin="round"/></svg></span></li>
    <li class="entry"><span class="kana">お</span><span class="reading">o<svg width="22" height="14" viewBox="0 0 22 14"><g fill="#b8996c"><circle cx="3" cy="3" r="2.2"/><circle cx="3" cy="11" r="2.2"/><circle cx="11" cy="11" r="2.2"/><circle cx="19" cy="11" r="2.2"/></g></svg></span><span class="script">Hiragana</span><span class="grade">K</span><span class="favourite"><svg width="30" height="30" viewBox="0 0 24 24"><path d="M12 2l2.9 6.6 7.1.6-5.4 4.7 1.6 7-6.2-3.7-6.2 3.7 1.6-7L2 9.2l7.1-.6z" fill="none" stroke="#b8996c" stroke-width="1.4" stroke-linejoin="round"/></svg></span></li>
    <li class="entry"><span class="kana">か</span><span class="reading">ka<svg width="22" height="14" viewBox="0 0 22 14"><g fill="#b8996c"><circle cx="3" cy="3" r="2.2"/><circle cx="3" cy="11" r="2.2"/><circle cx="11" cy="11" r="2.2"/><circle cx="19" cy="11" r="2.2"/></g></svg></span><span class="script">Hiragana</span><span class="grade">K</span><span class="favourite"><svg width="30" height="30" viewBox="0 0 24 24"><path d="M12 2l2.9 6.6 7.1.6-5.4 4.7 1.6 7-6.2-3.7-6.2 3.7 1.6-7L2 9.2l7.1-.6z" fill="none" stroke="#b8996c" stroke-width="1.4" stroke-linejoin="round"/></svg></span></li>
    <li class="entry"><span class="kana">が</span><span class="reading">ga<svg width="22" height="14" viewBox="0 0 22 14"><g fill="#b8996c"><circle cx="3" cy="3" r="2.2"/><circle cx="3" cy="11" r="2.2"/><circle cx="11" cy="11" r="2.2"/><circle cx="19" cy="11" r="2.2"/></g></svg></span><span class="script">Hiragana</span><span class="grade">K</span><span class="favourite"><svg width="30" height="30" viewBox="0 0 24 24"><path d="M12 2l2.9 6.6 7.1.6-5.4 4.7 1.6 7-6.2-3.7-6.2 3.7 1.6-7L2 9.2l7.1-.6z" fill="#b8996c" stroke="#b8996c" stroke-width="1.4" stroke-linejoin="round"/></svg></span></li>
  </ul>

  <footer class="tab-bar">
    <span class="home-button">Home</span>
    <span class="count">2278 entries found
      <svg width="26" height="16" viewBox="0 0 26 16"><polyline points="2,14 13,3 24,14" fill="none" stroke="#3b3026" stroke-width="2"/></svg>
    </span>
  </footer>
</main>
</body>
</html>
```